Product Page

We're marketing an on line educational product, and need a savvy designer to fix a web page that lacks pazazz. We're looking for a designer who can take a lot of information and present it neatly and elegantly, and put all the relevant testimonials in there without loosing cool factor. Right now we need just one page designed, but the winner will have the chance to re-do the entire site, with lots more content coming down the line that will need the new look.

The current page is here: www.kelmartune.com/sign-up. This should be combined with the attached PDF that has a lot more text information.

Note: The previous file listed as a pdf was a jpg. Sorry about that! Now there's a real pdf available for you to download.

I have added a jpg of myself. If you can use that I would appreciate it. I've also uploaded an example of a pricing page. Let me know how you would charge for this extra page.

Target Market(s)

Men and women in their forties who want to improve their singing but have other careers and are looking for high quality voice instruction.

The page must have an attractive "Get Started" button prominently displayed.

Industry/Entity Type

Marketing

Requirements
Must have
• Above the fold: clear buy now button, some testimonials, and the video. Should have a background that makes reading the text easy-not black. The new page must work somehow with the existing theme, although we will be re-designing the whole site soon with your help.
Nice to have
• Some navigation to organize a lot of text

```html
<!DOCTYPE html>
<html lang="en">
<head>
<meta charset="utf-8">
<title>Kel Martin School of Voice – Voice Ascent</title>
<link href="https://fonts.googleapis.com/css2?family=Open+Sans:wght@300;400;600;700&family=Oswald:wght@300;400;500&display=swap" rel="stylesheet">
<style>
:root{
  --blue:#2aa7de;
  --blue-dark:#1f8fc4;
  --navy:#1d4862;
  --navy-deep:#0f2f40;
  --footer:#102a38;
  --footer-bar:#0c3446;
  --nav:#3b4248;
  --ink:#333b41;
  --grey-text:#6a6f73;
  --light:#eceef0;
  --white:#fff;
}
*{box-sizing:border-box;margin:0;padding:0}
html,body{width:1200px;height:2318px;overflow:hidden}
body{font-family:"Open Sans",Arial,sans-serif;color:var(--ink);background:var(--white);position:relative}
.abs{position:absolute}
a{color:inherit;text-decoration:none}

/* header */
.topbar{left:0;top:0;width:1200px;height:29px;background:var(--blue);color:#fff;font-size:11px;font-weight:600;line-height:29px;padding-left:190px}
.navbar{left:0;top:29px;width:1200px;height:46px;background:var(--nav)}
.navbar ul{list-style:none;display:flex;gap:19px;padding-left:190px;line-height:46px}
.navbar li{font-family:"Oswald",sans-serif;font-size:13.5px;color:#fff;text-transform:uppercase;letter-spacing:.2px}
.navbar li.active{color:var(--blue)}
.logo-box{left:811px;top:0;width:149px;height:89px;background:#fff;border-bottom:6px solid var(--blue);box-shadow:0 2px 4px rgba(0,0,0,.25);display:flex;align-items:center;justify-content:center;gap:8px}
.logo-mark{width:22px;height:22px;background:var(--blue);border-radius:50%}
.logo-name{font-family:"Open Sans",sans-serif;font-size:17px;font-weight:600;color:var(--blue);line-height:1.1}
.logo-name small{display:block;font-size:10px}

/* hero */
.hero{left:0;top:75px;width:1200px;height:414px;background:linear-gradient(90deg,#8c8f92,#c7c9cb 40%,#b5b7ba 70%,#6f7376)}
.hero-card{left:189px;top:42px;width:819px;height:346px;background:#fff;clip-path:polygon(22px 0,100% 0,100% 100%,0 100%,0 22px)}
.hero-photo{left:0;top:0;width:357px;height:346px;background:linear-gradient(180deg,#d8d8d8,#6e6e6e 55%,#1e1e1e)}
.name-tag{left:-4px;top:285px;width:176px;height:52px;background:rgba(60,60,60,.85);color:#fff;text-align:center;font-family:"Oswald",sans-serif;font-weight:300}
.name-tag b{display:block;font-weight:300;font-size:19px;padding-top:5px}
.name-tag span{font-size:12.5px;font-family:"Open Sans",sans-serif}
.hero-text{left:330px;top:52px;width:470px;text-align:center}
.hero-text h1{font-family:"Oswald",sans-serif;font-weight:400;font-size:29px;color:var(--blue)}
.hero-text .sub{font-family:"Oswald",sans-serif;font-weight:300;font-size:20px;color:#333;margin-top:6px}
.hero-rule{margin:14px auto 0;width:447px;height:3px;background:#444;position:relative}
.hero-rule:after{content:"";position:absolute;left:50%;top:3px;margin-left:-8px;border:8px solid transparent;border-top-color:#444}
.hero-text .lead{font-family:"Oswald",sans-serif;font-weight:300;font-size:26px;line-height:1.38;color:#333;margin-top:26px}
.hero-text .lead b{font-weight:400;color:var(--blue)}

/* about */
.about{left:0;top:489px;width:1200px;height:365px;background:linear-gradient(180deg,#f1f2f3,#fff 60px)}
.about-text{left:190px;top:26px;width:425px}
.about-text h2{font-family:"Open Sans",sans-serif;font-weight:400;font-size:23px;color:#333}
.about-text .intro{font-size:15px;color:var(--blue);line-height:1.6;margin-top:10px}
.about-text .body{font-size:11.2px;color:var(--grey-text);line-height:1.95;margin-top:12px}
.btn{display:inline-block;font-family:"Oswald",sans-serif;font-size:19px;height:33px;line-height:33px;padding:0 13px;border-radius:3px}
.btn-grey{background:#dcdddf;color:#333;border:1px solid #c3c5c7}
.btn-blue{background:var(--blue);color:#fff;border:1px solid var(--blue-dark);margin-left:6px}
.btns{margin-top:14px}
.discount{font-size:14px;color:#8b8f93;margin-top:10px}
.video-frame{left:655px;top:29px;width:353px;height:231px;background:#c9d3d9;padding:8px}
.video{width:100%;height:100%;background:linear-gradient(180deg,#14252e,#0c1a21);display:flex;align-items:center;justify-content:center}

/* how / available */
.how{left:0;top:854px;width:650px;height:305px;background:var(--light)}
.how h2{position:absolute;left:190px;top:30px;font-weight:300;font-size:31px;line-height:1.25;color:#333}
.how h2 span{color:var(--blue)}
.how p{position:absolute;left:190px;top:126px;width:416px;font-size:11.2px;line-height:2.05;color:var(--grey-text)}
.how p a{color:var(--blue);font-weight:600;margin-left:14px}
.available{left:650px;top:854px;width:550px;height:305px;background:linear-gradient(90deg,#2b93cf 0%,#3aa2d9 55%,#6cbde6 100%)}
.available h2{position:absolute;left:32px;top:34px;font-weight:300;font-size:27px;line-height:1.38;color:#fff}
.available ul{position:absolute;left:32px;top:124px;list-style:none;color:#fff;font-size:12.5px;line-height:1.55;width:330px}
.available li{display:flex;gap:12px;margin-bottom:9px}
.available li svg{flex:none;margin-top:3px}

/* testimonials */
.reviews{left:0;top:1159px;width:1200px;height:415px;background:#fff;text-align:center}
.reviews h2{position:absolute;left:0;width:1200px;top:40px;font-size:20px;font-weight:400;color:var(--blue);letter-spacing:.5px}
.reviews .sub{position:absolute;left:300px;width:600px;top:78px;font-size:13px;color:#666;line-height:1.55}
.map{left:375px;top:122px;width:450px;height:130px;background:radial-gradient(ellipse at center,#eceef0 0%,#fff 70%)}
.avatars{left:486px;top:140px;display:flex;gap:15px}
.avatar{width:66px;height:66px;border:3px solid #fff;box-shadow:0 0 0 1px #d6d6d6}
.av1{background:linear-gradient(#9ab0c2,#6e7f8c)}
.av2{background:linear-gradient(#c0b7ad,#7b6e66)}
.av3{background:linear-gradient(#e6e1dc,#b9aea6)}
.quote{left:233px;top:233px;width:734px;height:144px;background:var(--blue);border-radius:3px;color:#fff;padding:22px 40px 0 55px}
.quote:before{content:"";position:absolute;left:50%;top:-13px;margin-left:-13px;border:13px solid transparent;border-top:0;border-bottom-color:var(--blue)}
.quote .mark{position:absolute;left:14px;top:12px;font-family:Georgia,serif;font-size:44px;font-weight:700;line-height:1}
.quote p{font-size:10.3px;line-height:2.1;font-weight:600}
.quote cite{display:block;font-style:normal;font-size:12.5px;margin-top:9px}

/* features */
.features{left:0;top:1574px;width:537px;height:459px;background:var(--light)}
.features .col{position:absolute;left:190px;top:18px;width:318px;font-size:11px;line-height:2.1;color:var(--grey-text)}
.features h3{font-weight:400;font-size:20px;color:var(--blue);line-height:1.2;margin-top:14px}
.features .small{font-size:10.5px;line-height:2}
.features .more{display:inline-block;margin-top:13px;color:var(--blue);font-size:14px;text-decoration:underline}
.systems{left:537px;top:1574px;width:663px;height:459px;background:var(--navy)}
.systems h2{position:absolute;left:26px;top:14px;font-weight:300;font-size:29px;color:#fff;line-height:1.2}
.systems h2 small{display:block;font-size:24px;color:var(--blue)}
.sys{position:absolute;width:210px;color:#fff}
.sys h4{display:flex;align-items:center;gap:9px;font-weight:400;font-size:17.5px}
.sys .ico{width:33px;height:33px;border-radius:50%;background:#d5dbe0;border:2px solid #fff}
.sys p{font-size:11px;font-weight:600;line-height:1.65;margin-top:6px}
.sys p a{color:var(--blue);font-weight:400;margin-left:4px}

/* footer */
.touch{left:500px;top:2062px;width:196px;height:42px;background:var(--blue);color:#fff;font-size:15px;text-align:center;line-height:42px;letter-spacing:.5px;z-index:2}
.footer{left:0;top:2078px;width:1200px;height:199px;background:var(--footer)}
.foot-list{position:absolute;top:57px;list-style:none;font-size:11px;color:#cfd8de;line-height:2}
.foot-list li:before{content:"";display:inline-block;border-left:5px solid var(--blue);border-top:3px solid transparent;border-bottom:3px solid transparent;margin-right:10px;transform:rotate(-45deg)}
.foot-about{position:absolute;left:509px;top:55px;width:252px}
.foot-about h4{font-weight:400;font-size:14.5px;color:var(--blue)}
.foot-about h4 b{color:#fff;font-weight:600}
.foot-about p{font-size:10.8px;line-height:1.8;color:#cfd8de;margin-top:8px}
.foot-about p a{color:var(--blue);margin-left:10px}
.foot-logo{position:absolute;left:830px;top:64px;display:flex;align-items:center;gap:10px}
.foot-logo .logo-name{color:#fff;font-size:19px}
.follow{position:absolute;left:830px;top:128px;color:#fff;font-size:13.5px;font-weight:600}
.socials{display:flex;gap:4px;margin-top:8px}
.socials span{width:18px;height:18px;border-radius:50%;background:var(--blue)}
.copy{left:0;top:2277px;width:1200px;height:41px;background:var(--footer-bar);color:#fff;font-size:11px;text-align:center;line-height:41px}
</style>
</head>
<body>

<header>
  <div class="abs topbar">Call Us : 555-014-2297 &nbsp;| &nbsp;Have an account? &nbsp;or &nbsp;Sign In</div>
  <nav class="abs navbar">
    <ul>
      <li class="active">Home</li><li>Voice Lessions</li><li>Blog</li><li>What Students Say</li><li>Meet the Instructors</li><li>Voice Ascent</li>
    </ul>
  </nav>
  <div class="abs logo-box">
    <span class="logo-mark"></span>
    <span class="logo-name">KelMartin<small>School of Voice</small></span>
  </div>
</header>

<section class="abs hero">
  <div class="abs hero-card">
    <div class="abs hero-photo" role="img" aria-label="Black and white portrait of the vocal coach in a dark turtleneck"></div>
    <div class="abs hero-text">
      <h1>Voice Ascent</h1>
      <p class="sub">The most technically advanced Platform for singers</p>
      <div class="hero-rule"></div>
      <p class="lead">Professional Vocal Coach, <b>Kel R. Martin</b> has laid the vocal foundation for thousands of singers worldwide, for 20+ years.</p>
    </div>
  </div>
  <div class="abs name-tag" style="left:185px;top:327px"><b>Kel Martin</b><span>Professional Voice Coach</span></div>
</section>

<section class="abs about">
  <div class="abs about-text">
    <h2>About Kel Martin School of Voice</h2>
    <p class="intro">Hi, I'm Kel Martin, the designer of Voice Ascent, and a professional voice coach based in the San Francisco Bay Area.</p>
    <p class="body">Phasellus vehicula vehicula sapien, ac tristique enim porta ac. Etiam risus ipsum, tincidunt non dapibus id, congue in nisl. Nunc consectetur gravida erat, aliquam congue augue ullamcorper sit amet. Aenean massa enim, suscipit eu elit vitae, commodo ultricies eros. Suspendisse ultrices feugiat nisl in rhoncus. Etiam mattis lacinia tellus, vel aliquam mauris rhoncus eget.</p>
    <div class="btns"><a class="btn btn-grey">Read More</a><a class="btn btn-blue">Get Started</a></div>
    <p class="discount">30% Discount Use Code : VB414</p>
  </div>
  <div class="abs video-frame">
    <div class="video" role="img" aria-label="Introduction video still of the vocal coach on a dark background">
      <svg width="62" height="62" viewBox="0 0 62 62"><circle cx="31" cy="31" r="29" fill="#2aa7de" stroke="#bfe6f7" stroke-width="3"/><path d="M25 18l14 13-14 13" fill="none" stroke="#1b2a33" stroke-width="7" stroke-linecap="round" stroke-linejoin="round"/></svg>
    </div>
  </div>
</section>

<section class="abs how">
  <h2>HOW VOICE<br><span>TRANSFORMATION</span> WORKS</h2>
  <p>After many years of work, I've decided that the effective transformation of the human voice is my life's work and passion. While on line methods of instruction are not as effective as in person lessons, I find that getting a foundational understanding of the voice that comes with Voice Ascent can greatly enhance your singing voice, whether you're currently studying with a teacher or working on your own. <a>Read More...</a></p>
</section>

<section class="abs available" role="img" aria-label="Blue toned photo of a smiling woman singing">
  <h2>VOICE ASCENT<br>AVAILABLE NOW</h2>
  <ul>
    <li><svg width="11" height="9" viewBox="0 0 11 9"><path d="M1 4.5l3 3 6-6" fill="none" stroke="#fff" stroke-width="2"/></svg>Get Instant Access</li>
    <li><svg width="11" height="9" viewBox="0 0 11 9"><path d="M1 4.5l3 3 6-6" fill="none" stroke="#fff" stroke-width="2"/></svg>Unique methods that are ideal for voice health</li>
    <li><svg width="11" height="9" viewBox="0 0 11 9"><path d="M1 4.5l3 3 6-6" fill="none" stroke="#fff" stroke-width="2"/></svg>The Most Advanced Platform for On Line Singing Instruction</li>
    <li><svg width="11" height="9" viewBox="0 0 11 9"><path d="M1 4.5l3 3 6-6" fill="none" stroke="#fff" stroke-width="2"/></svg>60+ Videos and Audio Workouts</li>
  </ul>
</section>

<section class="abs reviews">
  <h2>PEOPLE LOVE US. AND SO WILL YOU</h2>
  <p class="sub">Sed ut perspiciatis unde omnis iste natus error sit voluptatem accusantium doloremque laudantium, totam rem aperiam, eaque ipsa quae ab illo inventore.</p>
  <div class="abs map" role="img" aria-label="Faint world map behind the student photos"></div>
  <div class="abs avatars">
    <div class="avatar av1" role="img" aria-label="Student photo"></div>
    <div class="avatar av2" role="img" aria-label="Student photo"></div>
    <div class="avatar av3" role="img" aria-label="Student photo"></div>
  </div>
  <blockquote class="abs quote">
    <span class="mark">&ldquo;</span>
    <p>Sed ut perspiciatis unde omnis iste natus error sit voluptatem accusantium doloremque laudantium, totam rem aperiam, eaque ipsa quae ab illo inventore veritatis et quasi architecto beatae vitae dicta sunt explicabo. Nemo enim ipsam voluptatem quia voluptas sit aspernatur aut odit aut fugit, sed quia consequuntur magni dolores eos qui ratione voluptatem sequi nesciunt. Neque porro quisquam est, qui dolorem ipsum quia dolor sit amet, consectetur.</p>
    <cite>Mr. Michael, CEO Lorem Ipsum</cite>
  </blockquote>
</section>

<section class="abs features">
  <div class="col">
    <p>Vestibulum sed massa a lorem molestie dapibus nec sed magna. Nullam lobortis lectus ut felis viverra elementum. Pellentesque habitant morbi tristique senectus et netus et malesuada fames ac turpis egestas. Nunc viverra libero at pharetra congue. Suspendisse potenti.</p>
    <h3>Flexibility</h3>
    <p class="small">Vestibulum sed massa a lorem molestie dapibus nec sed magna. Nullam lobortis lectus ut felis viverra elementum.</p>
    <h3>Downloadable Content</h3>
    <p class="small">Vestibulum sed massa a lorem molestie dapibus nec sed magna. Nullam lobortis lectus ut felis viverra elementum.</p>
    <h3>Personal Interaction</h3>
    <p class="small">Vestibulum sed massa a lorem molestie dapibus nec sed magna. Nullam lobortis lectus ut felis viverra elementum.</p>
    <a class="more">View More...</a>
  </div>
</section>

<section class="abs systems">
  <h2>THE FIVE SYSTEMS.<small>Five essentials for a strong, free voice.</small></h2>
  <div class="sys" style="left:27px;top:92px"><h4><span class="ico"></span>Vocal Cords</h4><p>Lorem ipsum dolor sit amet, consec tetur adipiscing elitv estibulum soll icitudin. <a>Read More...</a></p></div>
  <div class="sys" style="left:263px;top:92px"><h4><span class="ico"></span>Air Control</h4><p>Lorem ipsum dolor sit amet, consec tetur adipiscing elitv estibulum soll icitudin. <a>Read More...</a></p></div>
  <div class="sys" style="left:27px;top:210px"><h4><span class="ico"></span>Outer Muscles</h4><p>Lorem ipsum dolor sit amet, consec tetur adipiscing elitv estibulum soll icitudin. <a>Read More...</a></p></div>
  <div class="sys" style="left:263px;top:210px"><h4><span class="ico"></span>Pharynx</h4><p>Lorem ipsum dolor sit amet, consec tetur adipiscing elitv estibulum soll icitudin. <a>Read More...</a></p></div>
  <div class="sys" style="left:27px;top:331px"><h4><span class="ico"></span>Outer Muscles</h4><p>Lorem ipsum dolor sit amet, consec tetur adipiscing elitv estibulum soll icitudin. <a>Read More...</a></p></div>
</section>

<a class="abs touch">GET IN TOUCH</a>
<footer class="abs footer">
  <ul class="foot-list" style="left:190px"><li>About us</li><li>Support</li><li>KRMMethod</li><li>Privacy Policy</li><li>Terms of use</li><li>Sitemap</li></ul>
  <ul class="foot-list" style="left:330px"><li>Home</li><li>Voice Lessions</li><li>Blog</li><li>What Students Say</li><li>Meet the Instructors</li><li>Voice Ascent</li></ul>
  <div class="foot-about">
    <h4>About <b>KelMartin</b> School of Voice</h4>
    <p>Lorem ipsum dolor sit amet, consectetur adipiscing elit. Maecenas vehicula imperdiet sapien at consequat. Nam ullamcorper sollicitudin nisi feugiat facilisis. Interdum et malesuada fames ac ante ipsum primis in faucibus. Pellentesque mi ipsum, bibendum. <a>Read More...</a></p>
  </div>
  <div class="foot-logo"><span class="logo-mark"></span><span class="logo-name">KelMartin<small>School of Voice</small></span></div>
  <div class="follow">Follow Us<div class="socials"><span></span><span></span><span></span><span></span></div></div>
</footer>
<div class="abs copy">© Copyright 2013. kelmartune.com</div>

</body>
</html>
```